Business Card Design Project

Basic business card with minimal details. I just need company name, email & web address, telephone and my name.
I would like the back of the card to be grey with my logo & company name centred.

Target Market(s)

Architects
Builders
Property Developers

Industry/Entity Type

Business

Font styles to use
Sans Serif

Colors

Designer to choose colors to be used in the design.

Requirements
Must have
• Venture Frame
Marcus Hadley - Director
M: 0452 913084
E: marcus@ventureframe.com.au
W: www.ventureframe.com.au
Should not have
• No other images or pictures

```html
<!DOCTYPE html>
<html lang="en">
<head>
<meta charset="utf-8">
<title>Venture Frame — Business Card</title>
<link rel="stylesheet" href="https://fonts.googleapis.com/css2?family=Lato:wght@400;700;900&display=swap">
<style>
  :root {
    --page-bg: #d9d4ce;
    --card-bg: #232323;
    --brand-grey: #4f5663;
    --brand-crimson: #a3173f;
    --contact-white: #f2f2f2;
    --card-shadow: 0 10px 24px rgba(0, 0, 0, 0.35);
  }
  * { margin: 0; padding: 0; box-sizing: border-box; }
  html, body {
    width: 1200px;
    height: 1000px;
    overflow: hidden;
    background: var(--page-bg);
    font-family: "Lato", sans-serif;
  }
  .canvas {
    position: relative;
    width: 1200px;
    height: 1000px;
  }
  .card {
    position: absolute;
    width: 800px;
    height: 400px;
    background: var(--card-bg);
    box-shadow: var(--card-shadow);
  }
  .card--front { left: 93px; top: 62px; }
  .card--back { left: 357px; top: 570px; }

  /* Front: name block */
  .holder {
    position: absolute;
    right: 76px;
    top: 56px;
    text-align: right;
  }
  .holder__name {
    font-weight: 900;
    font-size: 23px;
    letter-spacing: -0.3px;
    color: var(--brand-grey);
    line-height: 28px;
    text-transform: uppercase;
  }
  .holder__role {
    font-weight: 900;
    font-size: 19px;
    font-variant: small-caps;
    color: var(--brand-crimson);
    line-height: 24px;
  }

  /* Brand lockup */
  .brand {
    position: absolute;
    display: flex;
    align-items: center;
  }
  .brand__mark {
    background: var(--brand-crimson);
    flex: none;
  }
  .brand__name {
    font-weight: 400;
    color: var(--brand-grey);
    text-transform: uppercase;
    white-space: nowrap;
  }
  .card--front .brand { left: 60px; top: 150px; gap: 36px; }
  .card--front .brand__mark { width: 40px; height: 40px; }
  .card--front .brand__name { font-size: 38px; letter-spacing: 3px; }

  .card--back .brand {
    left: 0; right: 0; top: 60px;
    flex-direction: column;
    gap: 52px;
  }
  .card--back .brand__mark { width: 96px; height: 96px; }
  .card--back .brand__name { font-size: 50px; letter-spacing: 5px; }

  /* Contacts */
  .contacts {
    position: absolute;
    left: 64px;
    top: 254px;
    list-style: none;
  }
  .contacts__item {
    display: flex;
    align-items: center;
    height: 25.5px;
    font-size: 15px;
    color: var(--contact-white);
  }
  .contacts__icon {
    width: 29px;
    display: flex;
    align-items: center;
  }
  .contacts__icon svg { fill: none; stroke: var(--brand-crimson); }
</style>
</head>
<body>
<main class="canvas">

  <section class="card card--front" aria-label="Card front">
    <div class="holder">
      <p class="holder__name">Marcus Hadley</p>
      <p class="holder__role">Director</p>
    </div>

    <div class="brand">
      <span class="brand__mark" aria-hidden="true"></span>
      <span class="brand__name">Venture Frame</span>
    </div>

    <ul class="contacts">
      <li class="contacts__item">
        <span class="contacts__icon">
          <svg width="14" height="14" viewBox="0 0 14 14" aria-hidden="true">
            <path d="M5 2 L7 2 L7 5 L5.6 5.6 Q5.6 8 7 9 L7 12 L5 12 Q3 10 3 7 Q3 4 5 2 Z" fill="var(--brand-crimson)" stroke="none"/>
          </svg>
        </span>
        0452 913084
      </li>
      <li class="contacts__item">
        <span class="contacts__icon">
          <svg width="16" height="16" viewBox="0 0 16 16" aria-hidden="true">
            <circle cx="8" cy="8" r="7" fill="var(--brand-crimson)" stroke="none"/>
            <path d="M1.5 8 H14.5 M8 1 Q4.5 8 8 15 M8 1 Q11.5 8 8 15" stroke="var(--card-bg)" stroke-width="1"/>
          </svg>
        </span>
        www.ventureframe.com.au
      </li>
      <li class="contacts__item">
        <span class="contacts__icon">
          <svg width="16" height="12" viewBox="0 0 16 12" aria-hidden="true">
            <rect x="0.75" y="1.5" width="14.5" height="9.5" stroke-width="1.3"/>
            <path d="M0.75 1.5 L8 7 L15.25 1.5" stroke-width="1.3"/>
          </svg>
        </span>
        marcus@ventureframe.com.au
      </li>
    </ul>
  </section>

  <section class="card card--back" aria-label="Card back">
    <div class="brand">
      <span class="brand__mark" aria-hidden="true"></span>
      <span class="brand__name">Venture Frame</span>
    </div>
  </section>

</main>
</body>
</html>
```